Nur Briefpapier und VK für Pflegedienst, Logo vorhanden!!!!
Zielgruppe
Wir sind ein Pflegedienst, unsere Zielgruppe sind Krankenkassen und Patienten und andere Krankenhäuser mit denen wir zusammen arbeiten.
Aufgabenstellung
modern, seriös, elitär

```html
<!DOCTYPE html>
<html lang="de">
<head>
<meta charset="utf-8">
<title>Fenrokare Pflegedienste – Visitenkarte</title>
<link href="https://fonts.googleapis.com/css2?family=Roboto:wght@300;400;700;900&family=Roboto+Condensed:wght@300&display=swap" rel="stylesheet">
<style>
  :root {
    --brand-red: #e0102b;
    --ink: #2b2b2b;
    --paper: #ffffff;
    --page: #ffffff;
  }
  * { margin: 0; padding: 0; box-sizing: border-box; }
  html, body {
    width: 914px; height: 1200px; overflow: hidden;
    background: var(--page);
    font-family: "Roboto", sans-serif;
  }
  .card {
    position: absolute; left: 27px; width: 861px; height: 564px;
    box-shadow: 0 1px 4px rgba(0,0,0,.35);
    overflow: hidden;
  }
  /* Front */
  .card--front { top: 24px; background: var(--brand-red); color: var(--paper); }
  .front-brand {
    position: absolute; left: 0; right: 0; top: 190px;
    text-align: center; font-weight: 700; font-size: 84px; letter-spacing: 1px;
    font-family: "Roboto", sans-serif;
  }
  .front-tagline {
    position: absolute; left: 0; right: 0; top: 462px;
    text-align: center; font-family: "Roboto Condensed", sans-serif;
    font-weight: 300; font-size: 54px;
  }
  /* Back */
  .card--back { top: 611px; background: var(--paper); }
  .back-band { position: absolute; inset: 0; width: 861px; height: 564px; }
  .slogan {
    position: absolute; left: 54px; top: 80px;
    color: var(--paper); font-weight: 700; font-size: 23px; letter-spacing: .3px;
    transform: rotate(-7.5deg); transform-origin: left bottom; white-space: nowrap;
  }
  .back-brand {
    position: absolute; left: 640px; width: 176px; top: 128px;
    text-align: center; color: var(--brand-red);
    font-weight: 700; font-size: 31px;
  }
  .back-sub {
    position: absolute; left: 640px; width: 176px; top: 273px;
    text-align: center; color: var(--brand-red);
    font-family: "Roboto Condensed", sans-serif; font-weight: 300; font-size: 26px;
  }
  .person { position: absolute; left: 66px; top: 281px; color: var(--ink); }
  .person-name { font-weight: 700; font-size: 29px; line-height: 34px; letter-spacing: .3px; }
  .person-role { font-weight: 400; font-size: 25px; line-height: 34px; }
  .contact { position: absolute; left: 66px; top: 388px; color: var(--ink); font-size: 25px; font-weight: 300; }
  .contact-line { line-height: 34.5px; white-space: nowrap; display: flex; align-items: center; gap: 8px; }
  .contact-line svg { width: 19px; height: 19px; fill: var(--ink); }
  .services {
    position: absolute; right: 53px; top: 402px; text-align: right;
    color: var(--brand-red); font-size: 24px; font-weight: 300; list-style: none;
  }
  .services li { line-height: 42px; }
</style>
</head>
<body>

<section class="card card--front">
  <div class="front-brand">Fenrokare</div>
  <div class="front-tagline">Pflegedienste</div>
</section>

<section class="card card--back">
  <svg class="back-band" viewBox="0 0 968 635" preserveAspectRatio="none" aria-hidden="true">
    <path fill="var(--brand-red)" d="M0 0 H968 V122 C930 108 900 96 860 84 L720 79 C580 80 430 108 300 128 C190 146 80 152 0 141 Z"/>
    <rect x="720" y="38" width="197" height="200" rx="12" fill="var(--paper)"/>
  </svg>

  <div class="slogan">Schutz im Zeichen der Fürsorge</div>

  <div class="back-brand">Fenrokare</div>
  <div class="back-sub">Pflegedienste</div>

  <div class="person">
    <div class="person-name">Max Mustermann</div>
    <div class="person-role">Pflegefachkraft</div>
  </div>

  <div class="contact">
    <div class="contact-line">Lindenhof 42</div>
    <div class="contact-line">45127 Essen</div>
    <div class="contact-line">
      <svg viewBox="0 0 24 24" aria-hidden="true"><path d="M6.6 10.8a15.1 15.1 0 0 0 6.6 6.6l2.2-2.2c.3-.3.7-.4 1-.2 1.1.4 2.3.6 3.6.6.6 0 1 .4 1 1V20c0 .6-.4 1-1 1A17 17 0 0 1 3 4c0-.6.4-1 1-1h3.5c.6 0 1 .4 1 1 0 1.3.2 2.5.6 3.6.1.3 0 .7-.2 1z"/></svg>
      <span>0201 - 47 28 350</span>
    </div>
    <div class="contact-line">
      <svg viewBox="0 0 24 24" aria-hidden="true"><path d="M2 5h20v14H2z M4 7v.5l8 5 8-5V7l-8 5z" fill-rule="evenodd"/></svg>
      <span>kontakt@email.de</span>
    </div>
  </div>

  <ul class="services">
    <li>Kinder-, Alten- und Krankenpflege</li>
    <li>Ambulante Intensivkrankenpflege</li>
    <li>Seminare und Schulungen</li>
    <li>Soziale Dienste</li>
  </ul>
</section>

</body>
</html>
```